Construction Company informative web page

Lorvane Builders is a new company that combine Project Manager and kitchen & bath design with Interior remodeling for houses or business (commercial and residential construction)
We want to show our reviews, portafolio and background experience
Updates

Reason: I would like to have the time to interact with the favorite designers to fine tune the website also I'd like to see more designs

Hello Everybody,

Thank you for your time, please make the corrections shown below:

Pages:

1. Home:

1.  Includes a welcome and a briefly background:

2. Right side vertically show a few reviews with the option read more to open it, just the Name and last name, city and review (no start ratings)

3. Facebook and youtube link

4. Left side below shows 4 slides show with pictures and titles:

1. Kitchen Design

2. Bath Design

3. General Remodeling

4. Commercial Projects

2. About Us:

Our Professionals:

Lorvane Builders Project Manager  is responsible to set the project schedule, request materials  and coordinate the delivery on time.  The Project Manager focus is ensuring  the best customer satisfaction in every step of the project until the final product is completed.

The Designer gives you the best ideas in 3D format,   getting the best lay out possible.  understanding your needs, defining your unique style putting together all your requirements and ideas to make the best match for you, making sure you get the best products within your budget

Lorvane Builders have a high quality group of trade specialist; plumbers, electricians and installers. Our crew is pleasant to work with,  safety and cleaning values  and very detailed oriented

Our Core Values

As our slogan your project is our business, well we really mean it our job is not just to do the job is to guaranteed a pleasant experience with great costumer service, communication, quality, in time and within your budget

 

1. Services:

1. Commercial

2. Residential

2. Portafolio:  Separated pictures in each project, I want to have a brief description in each picture

1. Kitchen Design

2. Bath Design

3. General Remodeling

4. Commercial Projects

 

1. Contact Us:  

1. Project Management Department:

Contact Person: Tessa Kobrin

Email: tessa@lorvanebuilders.com

2. Office Management Department:

Contact Person: Rue Fendwick

Email: info@lorvanebuilders.com

 

Please try to pick design style shown in business card to match a little bit. Keep the color tones

I want the logo in the upper left corner and a very nice picture with a kitchen (warm colors)mostly American northeast style like the main pic of the web.

I want the web page is able to be fully open in computers, tablets and cellphones

Please send me an email to lorvanebuild7@mailbrook.net so I can send you my logo and any other information to be incorporated

Thank you

Hello Everybody,

Thank you for your time, please make the corrections accordingly:

Pages:

1. Home: Includes a welcome and a briefly say something about our background 

Hello, I just upload my logo and my business card so you can adjust your designs

Please presented responsive format

I want coding the webpage too

Please read carefully my last update

Thank you so much!                                   

Industry/Entity Type

Residential

Requirements
Nice to have
• Should it has a Newsletter subscription with the email at the bottom of the home page
In contact page: A box "Contact us for a free estimate"

```html
<!DOCTYPE html>
<html lang="en">
<head>
<meta charset="utf-8">
<title>Lorvane Builders — Commercial &amp; Residential Construction</title>
<link href="https://fonts.googleapis.com/css2?family=Questrial&family=Arimo:wght@400;700&family=Noto+Serif:ital@1&display=swap" rel="stylesheet">
<style>
:root{
  --wine:#7a2323;
  --wine-dark:#5e1616;
  --tan:#e2c48c;
  --tan-light:#efdcb3;
  --cream:#fdf9f1;
  --panel:#f3ece0;
  --panel-border:#e4dccd;
  --ink:#3a2a22;
  --body-text:#4a3d35;
  --footer:#2a1c10;
  --footer-base:#1e140b;
  --footer-text:#d8cbb4;
  --head-font:'Questrial',sans-serif;
  --body-font:'Arimo',sans-serif;
  --quote-font:'Noto Serif',serif;
}
*{margin:0;padding:0;box-sizing:border-box}
html,body{width:1105px;height:1200px;overflow:hidden}
body{position:relative;background:var(--cream);font-family:var(--body-font);color:var(--body-text)}

.site-header{position:absolute;left:0;top:0;width:1105px;height:108px;background:var(--wine);border-bottom:2px solid #963737}
.brand{position:absolute;left:151px;top:22px;display:flex;align-items:center;gap:12px}
.brand-mark{width:60px;height:60px;background:var(--tan-light)}
.brand-name{font-family:var(--head-font);font-size:21px;color:var(--tan-light);letter-spacing:.5px;text-transform:uppercase;line-height:1.2}
.brand-tagline{font-family:var(--body-font);font-size:13px;color:var(--tan-light);margin-top:2px}
.header-phone{position:absolute;right:151px;top:34px;display:flex;align-items:center;gap:7px;color:#fff;font-weight:700;font-size:18px}
.social{display:flex;gap:6px}
.social span{width:25px;height:25px;border-radius:50%;background:var(--tan);display:block}
.header-social{position:absolute;right:151px;top:69px}

.main-nav{position:absolute;left:0;top:108px;width:1105px;height:52px;background:var(--tan)}
.main-nav ul{list-style:none;display:flex;justify-content:center;align-items:center;height:46px;font-family:var(--head-font);font-size:14px;color:var(--ink);text-transform:uppercase}
.main-nav li{display:flex;align-items:center}
.main-nav li+li::before{content:"";width:7px;height:7px;border-radius:50%;background:var(--wine);margin:0 20px}

.hero{position:absolute;left:0;top:158px;width:1105px;height:356px;background:linear-gradient(180deg,#7a4a28 0%,#a46a3a 35%,#6a3e20 70%,#2c1a10 100%)}
.hero-curve{position:absolute;left:0;top:150px;width:1105px;height:26px}
.hero-title{position:absolute;left:0;width:100%;top:244px;text-align:center;color:#fff;font-family:var(--head-font);text-transform:uppercase;line-height:1.1}
.hero-title .line-light{font-size:34px;letter-spacing:1px}
.hero-title .line-bold{font-size:34px;font-weight:700;font-family:var(--body-font);letter-spacing:.5px}
.hero-dots{position:absolute;top:488px;left:0;width:100%;display:flex;justify-content:center;gap:6px}
.hero-dots span{width:10px;height:10px;border-radius:50%;background:var(--tan)}
.hero-dots span.active{background:#c8282a}

.section-title{position:absolute;left:151px;font-family:var(--head-font);font-size:24px;color:#2a1a14;text-transform:uppercase}
.section-title::after{content:"";position:absolute;left:0;top:36px;width:151px;height:2px;background:var(--wine)}
.welcome-title{top:532px}
.work-title{top:694px}
.body-copy{font-size:12px;line-height:19.3px}
.welcome-copy{position:absolute;left:151px;top:581px;width:525px}
.work-heading{position:absolute;left:153px;top:743px;font-family:var(--head-font);font-size:17.5px;color:var(--wine)}
.work-photo{position:absolute;left:151px;top:777px;width:249px;height:171px;border:2px solid #ddd;background:linear-gradient(135deg,#b99a72,#7a5a3c 55%,#d8ccb4)}
.work-copy{position:absolute;left:414px;top:779px;width:264px}
.btn{position:absolute;left:414px;top:886px;width:99px;height:28px;background:var(--wine);color:#fff;font-size:12px;display:flex;align-items:center;justify-content:center;border-radius:2px}

.quote-cta{position:absolute;left:704px;top:530px;width:250px;height:62px;background:var(--wine);border:3px solid var(--wine-dark);box-shadow:inset 0 0 0 2px #a65050;display:flex;align-items:center;padding-left:16px;gap:14px;color:var(--tan-light);font-family:var(--head-font);font-size:20px;text-transform:uppercase}
.quote-cta b{font-family:var(--body-font);font-weight:700}
.testimonials{position:absolute;left:704px;top:606px;width:250px;height:361px;background:var(--panel);border:3px solid var(--panel-border)}
.testimonials .quote-mark{position:absolute;left:12px;top:-4px;font-family:var(--quote-font);font-size:80px;color:#d8ccb8;line-height:1}
.testimonials h2{position:absolute;left:78px;top:27px;font-family:var(--head-font);font-weight:400;font-size:24px;color:var(--wine);text-transform:uppercase}
.testimonials blockquote{position:absolute;left:14px;top:60px;width:220px;font-family:var(--quote-font);font-style:italic;font-size:12px;line-height:17.3px;color:#3a2e28}
.testimonials blockquote p+p{margin-top:17px}
.reviewer{position:absolute;left:14px;top:278px;display:flex;gap:9px}
.reviewer-photo{width:61px;height:61px;background:linear-gradient(160deg,#ece6dc,#b9aa98)}
.reviewer-name{font-family:var(--head-font);font-size:15px;color:var(--wine);margin-top:3px}
.reviewer-place{font-size:11px;color:#666;margin-top:2px}

.site-footer{position:absolute;left:0;top:980px;width:1105px;height:172px;background:var(--footer);border-top:4px solid #efe6d6}
.footer-brand{top:26px}
.footer-contact{position:absolute;left:240px;top:104px;display:grid;grid-template-columns:138px 180px;row-gap:12px;font-size:13.5px;color:var(--footer-text)}
.footer-contact div{display:flex;align-items:center;gap:12px}
.footer-social{position:absolute;right:151px;top:57px}
.footer-nav{position:absolute;right:151px;top:104px;text-align:right;font-size:13.5px;line-height:19px;color:var(--footer-text)}
.footer-nav .sep{margin:0 6px}
.copyright{position:absolute;left:0;top:1152px;width:1105px;height:48px;background:var(--footer-base);color:#d8d0c2;font-size:10.5px;display:flex;align-items:center;justify-content:center}
</style>
</head>
<body>

<header class="site-header">
  <div class="brand">
    <div class="brand-mark"></div>
    <div>
      <div class="brand-name">Lorvane Builders</div>
      <div class="brand-tagline">Your project is our business</div>
    </div>
  </div>
  <div class="header-phone">
    <svg width="15" height="15" viewBox="0 0 24 24"><path fill="#e2c48c" d="M6.6 10.8a15 15 0 0 0 6.6 6.6l2.2-2.2c.3-.3.7-.4 1-.2 1.1.4 2.3.6 3.6.6.6 0 1 .4 1 1V20c0 .6-.4 1-1 1A17 17 0 0 1 3 4c0-.6.4-1 1-1h3.5c.6 0 1 .4 1 1 0 1.3.2 2.5.6 3.6.1.3 0 .7-.2 1z"/></svg>
    215-555-0182
  </div>
  <div class="social header-social"><span></span><span></span><span></span></div>
</header>

<nav class="main-nav">
  <ul>
    <li>Home</li><li>About Us</li><li>Our Work</li><li>Request a Quote</li><li>Meet Our Team</li><li>Contact Us</li>
  </ul>
</nav>

<div class="hero" role="img" aria-label="Warm-toned kitchen with wood cabinets, tiled backsplash and granite counters"></div>
<svg class="hero-curve" viewBox="0 0 1105 26" preserveAspectRatio="none"><path d="M0 0H1105V8C700 8 300 2 0 14Z" fill="#e2c48c"/></svg>
<div class="hero-title">
  <div class="line-light">Commercial &amp; Residential General</div>
  <div class="line-bold">Construction Kitchen &amp; Bath Design</div>
</div>
<div class="hero-dots"><span class="active"></span><span></span><span></span></div>

<main>
  <h2 class="section-title welcome-title">Welcome</h2>
  <p class="body-copy welcome-copy">Lorem ipsum dolor sit amet, consectetur adipiscing elit. Ut sit amet metus ut lorem pharetra venenatis fermentum at nibh. Nulla aliquet diam eu turpis convallis sit amet malesuada mi ultrices. In in velit massa, vitae condimentum leo. Vivamus nulla sapien, bibendum eget malesuada eget, volutpat nec nisl. Aenean turpis magna, dapibus a laoreet a, eleifend eget metus. Vestibulum quis interdum lacus.</p>

  <h2 class="section-title work-title">Latest Work</h2>
  <h3 class="work-heading">Maecenas ultrices eros eget justo ultricies in mollis</h3>
  <div class="work-photo" role="img" aria-label="Granite kitchen counter with copper sink and bronze faucet"></div>
  <p class="body-copy work-copy">Lorem ipsum dolor sit amet, consectetur adipiscing elit. Ut sit amet metus ut lorem pharetra venenatis fermentum at nibh. Nulla aliquet diam eu turpis convallis sit amet malesuada mi ultrices. In in velit massa.</p>
  <a class="btn">Learn More</a>

  <aside>
    <div class="quote-cta">
      <span>Request a <b>Quote</b></span>
      <svg width="34" height="32" viewBox="0 0 34 32"><path d="M2 2H32V22H14L6 30V22H2Z" fill="#efdcb3"/><rect x="8" y="8" width="18" height="2" fill="#7a2323"/><rect x="8" y="13" width="14" height="2" fill="#7a2323"/></svg>
    </div>
    <section class="testimonials">
      <span class="quote-mark">&ldquo;</span>
      <h2>Testimonials</h2>
      <blockquote>
        <p>Lorem ipsum dolor sit amet, consectetur adipiscing elit. Ut sit amet metus ut lorem pharetra venenatis fermentum at nibh.</p>
        <p>Nulla aliquet diam eu turpis convallis sit amet malesuada mi ultrices. In in velit massa, vitae condimentum leo. Vivamus nulla sapien, bibendum eget malesuada eget, volutpat nec nisl. Aenean turpis magna, dapibus a laoreet a, eleifend eget metus.</p>
      </blockquote>
      <div class="reviewer">
        <div class="reviewer-photo" role="img" aria-label="Portrait of the reviewer"></div>
        <div>
          <div class="reviewer-name">Dorian Vale</div>
          <div class="reviewer-place">USA</div>
        </div>
      </div>
    </section>
  </aside>
</main>

<footer class="site-footer">
  <div class="brand footer-brand">
    <div class="brand-mark"></div>
    <div>
      <div class="brand-name">Lorvane Builders</div>
      <div class="brand-tagline">Your project is our business</div>
    </div>
  </div>
  <div class="footer-contact">
    <div><svg width="14" height="14" viewBox="0 0 24 24"><path fill="#8a7250" d="M6.6 10.8a15 15 0 0 0 6.6 6.6l2.2-2.2c.3-.3.7-.4 1-.2 1.1.4 2.3.6 3.6.6.6 0 1 .4 1 1V20c0 .6-.4 1-1 1A17 17 0 0 1 3 4c0-.6.4-1 1-1h3.5c.6 0 1 .4 1 1 0 1.3.2 2.5.6 3.6.1.3 0 .7-.2 1z"/></svg>215-555-0182</div>
    <div><svg width="10" height="16" viewBox="0 0 10 16"><rect x="0.5" y="0.5" width="9" height="15" rx="1.5" fill="none" stroke="#8a7250"/><rect x="4" y="12" width="2" height="2" fill="#8a7250"/></svg>856-555-0147</div>
    <div><svg width="15" height="14" viewBox="0 0 15 14"><rect x="3" y="0" width="9" height="4" fill="#8a7250"/><rect x="0" y="4" width="15" height="6" rx="1" fill="#8a7250"/><rect x="3" y="9" width="9" height="5" fill="#a58a64"/></svg>215-555-0196</div>
    <div><svg width="15" height="11" viewBox="0 0 15 11"><rect width="15" height="11" fill="#8a7250"/><path d="M0 0L7.5 6L15 0" fill="none" stroke="#2a1c10" stroke-width="1.2"/></svg>tessa@lorvanebuilders.com</div>
  </div>
  <div class="social footer-social"><span></span><span></span><span></span></div>
  <nav class="footer-nav">
    <div>Home<span class="sep">|</span>About Us<span class="sep">|</span>Our Work<span class="sep">|</span>Request a Quote</div>
    <div>Meet Our Team<span class="sep">|</span>Contact Us</div>
  </nav>
</footer>
<div class="copyright">Copyright © 2014 lorvanebuilders.com. All Rights Reserved.</div>

</body>
</html>
```